Tide 4 Tide letterhead design and business card design for electrical company

I need a letterhead that can be used for my invoices and quote books along with emails sent to clients. I have a logo and the logo of Guild tradespeople I just need all my information placed nicely with a good flow.

Business Name: Tide 4 Tide Electrical
Name: Darren Kolvetis
Abn: 57804219362
Licence Number: 39417
Number: 0400683541

Thank you in advanced

Target Market(s)

Electrical Clients

Industry/Entity Type

Business

Contact Information for Business Card

Name: Darren Kolvetis
Abn: 57804219362
Licence Number: 39417
Number: 0400683541

Font styles to use
Sans Serif

Colors

Designer to choose colors to be used in the design.

Requirements
Must have
• Must have my logo, guild tradespeople logo even if its smaller and in the corner and all details
Nice to have
• Domestic Commercial Industrial stated on there somewhere

```html
<!DOCTYPE html>
<html lang="en">
<head>
<meta charset="UTF-8">
<title>Tide 4 Tide Electrical – Letterhead</title>
<link href="https://fonts.googleapis.com/css2?family=Open+Sans:wght@400;600;700&display=swap" rel="stylesheet">
<style>
  :root {
    --backdrop: #e4e4e4;
    --paper: #ffffff;
    --brand-blue: #1a4fa3;
    --ink-dark: #2b2b2e;
    --ink-soft: #55575c;
    --badge-navy: #1d2f4d;
    --rule: #8a8c90;
  }
  * { box-sizing: border-box; margin: 0; padding: 0; }
  html, body {
    width: 1200px; height: 1200px; overflow: hidden;
    background: var(--backdrop);
    font-family: "Open Sans", sans-serif;
  }
  .letterhead {
    position: absolute; left: 220px; top: 62px;
    width: 760px; height: 1075px;
    background: var(--paper);
    box-shadow: 0 6px 24px rgba(0,0,0,0.12);
    overflow: hidden;
  }
  .brand {
    position: absolute; left: 64px; top: 62px;
    display: flex; align-items: center; gap: 12px;
  }
  .brand-mark {
    width: 30px; height: 30px; background: var(--brand-blue); border-radius: 4px;
  }
  .brand-name {
    font-family: "Open Sans", sans-serif;
    font-weight: 700; font-size: 21px; color: var(--brand-blue);
    letter-spacing: 0.3px;
  }
  .contact {
    position: absolute; left: 548px; top: 48px;
    padding-left: 14px;
    border-left: 1px solid var(--rule);
    font-size: 9.5px; line-height: 14px; color: var(--ink-dark);
    font-style: normal;
  }
  .contact .address { margin-bottom: 4px; }
  .contact-line { display: flex; align-items: center; gap: 6px; }
  .contact-line svg { width: 9px; height: 9px; flex: none; }
  .member-badge {
    position: absolute; left: 110px; top: 900px;
    width: 42px; height: 42px; border-radius: 5px;
    background: var(--badge-navy);
  }
  .footer-band {
    position: absolute; left: 0; bottom: 0; width: 760px; height: 140px;
  }
  .registration {
    position: absolute; right: 26px; bottom: 42px;
    font-size: 10px; line-height: 14px; color: #ffffff; letter-spacing: 0.2px;
    white-space: nowrap;
  }
  .registration .divider { margin: 0 8px; opacity: 0.8; }
</style>
</head>
<body>
  <main class="letterhead">
    <header class="brand">
      <span class="brand-mark"></span>
      <span class="brand-name">Tide 4 Tide Electrical</span>
    </header>

    <address class="contact">
      <div class="address">55 demo street, demo place<br>P.O. Box 000, 555 Avenue</div>
      <div class="contact-line">
        <svg viewBox="0 0 10 10"><path d="M2 1 L4 1 L4.6 3.2 L3.4 4 C4 5.4 4.8 6.2 6 6.6 L6.8 5.4 L9 6 L9 8 C9 8.6 8.6 9 8 9 C4.2 8.8 1.2 5.8 1 2 C1 1.4 1.4 1 2 1Z" fill="var(--brand-blue)"/></svg>
        <span>0400683541</span>
      </div>
      <div class="contact-line">
        <svg viewBox="0 0 10 10"><rect x="0.5" y="2" width="9" height="6" rx="1" fill="var(--brand-blue)"/><path d="M0.8 2.4 L5 5.4 L9.2 2.4" stroke="#fff" stroke-width="0.8" fill="none"/></svg>
        <span>info@websitename.com</span>
      </div>
      <div class="contact-line">
        <svg viewBox="0 0 10 10"><circle cx="5" cy="5" r="4.2" fill="none" stroke="var(--brand-blue)" stroke-width="1"/><ellipse cx="5" cy="5" rx="1.8" ry="4.2" fill="none" stroke="var(--brand-blue)" stroke-width="0.8"/><line x1="0.8" y1="5" x2="9.2" y2="5" stroke="var(--brand-blue)" stroke-width="0.8"/></svg>
        <span>www.websitename.com</span>
      </div>
    </address>

    <div class="member-badge" role="img" aria-label="Guild tradespeople member badge"></div>

    <svg class="footer-band" viewBox="0 0 760 140" aria-hidden="true">
      <path d="M0 106 L388 106 C425 106 430 46 470 42 L760 36" fill="none" stroke="var(--ink-dark)" stroke-width="4"/>
      <path d="M0 118 L400 118 C440 118 445 60 485 56 L760 52 L760 140 L0 140 Z" fill="var(--brand-blue)"/>
    </svg>

    <div class="registration">Abn: 57804219362<span class="divider">|</span>Licence Number: 39417</div>
  </main>
</body>
</html>
```